Brivane - Business Cards for a new venture

create business card for a startup classified business dealing in construction materials, the cards need to have a professional look but modern, more serious than playful, one of the samples must include the official font (attached), please explore using the official colors in the company's logo

Target Market(s)

Energy sector

Contact Information for Business Card

Font styles to use
Other font styles liked:
• suissnord

Requirements
Must have
• corporate colors (in logo attached)
Nice to have
• Official font (in one of the samples) font is : suissnord
Should not have
• Cartoonish look

```html
<!DOCTYPE html>
<html lang="en">
<head>
<meta charset="utf-8">
<title>Brivane – Business Cards</title>
<link href="https://fonts.googleapis.com/css2?family=Lato:wght@300;400;700&display=swap" rel="stylesheet">
<style>
  :root{
    --backdrop:#2b2b2d;
    --navy:#0d4680;
    --slate:#97989c;
    --paper:#ffffff;
    --ink-light:#f2f3f5;
    --band-gap:#8d8e92;
  }
  *{box-sizing:border-box;margin:0;padding:0}
  html,body{width:1200px;height:900px;overflow:hidden;background:var(--backdrop);font-family:"Lato",Arial,sans-serif}
  .canvas{position:relative;width:1200px;height:900px}
  .card{position:absolute;width:600px;height:343px;border-radius:18px;overflow:hidden;box-shadow:0 14px 30px rgba(0,0,0,.45)}

  /* front */
  .card-front{left:60px;top:70px;background:var(--slate)}
  .front-edge{position:absolute;left:0;top:0;width:30px;height:100%;background:var(--navy)}
  .front-brand-panel{position:absolute;left:30px;top:0;width:262px;height:100%;background:var(--paper);display:flex;align-items:center;justify-content:center}
  .brand-tab{position:absolute;left:262px;width:48px;background:var(--navy)}
  .brand-tab--top{top:0;height:70px}
  .brand-tab--bottom{bottom:0;height:108px;top:auto;clip-path:polygon(0 20%,100% 20%,100% 100%,0 100%)}
  .wordmark{font-weight:300;letter-spacing:.22em;text-transform:uppercase;display:flex;align-items:center;gap:12px}
  .wordmark-dot{border-radius:50%;display:inline-block}
  .front-brand-panel .wordmark{color:var(--navy);font-size:30px}
  .front-brand-panel .wordmark-dot{width:14px;height:14px;background:var(--navy)}

  .holder{position:absolute;left:326px;top:14px;color:var(--ink-light)}
  .holder-name{font-weight:700;font-size:21px;line-height:1.1}
  .holder-role{font-weight:400;font-size:13px;margin-top:2px}

  .contact-list{position:absolute;left:310px;top:72px;width:290px;list-style:none}
  .contact-item{height:37px;margin-bottom:4px;background:var(--navy);display:flex;align-items:center;gap:12px;padding-left:22px;color:var(--ink-light);font-size:15px}
  .contact-icon{width:16px;height:16px;fill:var(--ink-light);flex:none}
  .address{position:absolute;left:332px;top:250px;color:var(--ink-light);font-size:14.5px;line-height:1.45}

  /* back */
  .card-back{left:540px;top:490px;background:var(--slate);display:flex;align-items:center;justify-content:center}
  .card-back .wordmark{color:var(--paper);font-size:46px}
  .card-back .wordmark-dot{width:20px;height:20px;background:var(--paper)}
</style>
</head>
<body>
<main class="canvas">

  <section class="card card-front" aria-label="Business card front">
    <div class="front-edge"></div>
    <div class="front-brand-panel">
      <div class="wordmark"><span class="wordmark-dot"></span>Brivane</div>
    </div>
    <div class="brand-tab brand-tab--top"></div>
    <div class="brand-tab brand-tab--bottom"></div>

    <header class="holder">
      <h1 class="holder-name">Alder Quinn</h1>
      <p class="holder-role">President</p>
    </header>

    <ul class="contact-list">
      <li class="contact-item">
        <svg class="contact-icon" viewBox="0 0 24 24"><path d="M6.6 10.8a15.1 15.1 0 0 0 6.6 6.6l2.2-2.2a1 1 0 0 1 1-.25 11.4 11.4 0 0 0 3.6.57 1 1 0 0 1 1 1V20a1 1 0 0 1-1 1A17 17 0 0 1 3 4a1 1 0 0 1 1-1h3.5a1 1 0 0 1 1 1c0 1.25.2 2.45.57 3.57a1 1 0 0 1-.25 1z"/></svg>
        (555) 280-0147
      </li>
      <li class="contact-item">
        <svg class="contact-icon" viewBox="0 0 24 24"><path d="M7 2h8l3 3v5H7zM4 11h16a2 2 0 0 1 2 2v6H2v-6a2 2 0 0 1 2-2zm3 10h10v-2H7z"/></svg>
        (555) 280-0148
      </li>
      <li class="contact-item">
        <svg class="contact-icon" viewBox="0 0 24 24"><path d="M2 5h20v14H2zm2 2v.5l8 5.5 8-5.5V7l-8 5.5z"/></svg>
        info@brivane.com
      </li>
      <li class="contact-item">
        <svg class="contact-icon" viewBox="0 0 24 24"><path d="M12 2a10 10 0 1 0 0 20 10 10 0 0 0 0-20zm-1 2.1V8H7.4A8 8 0 0 1 11 4.1zm2 0A8 8 0 0 1 16.6 8H13zM4.6 10H11v4H4.6a8 8 0 0 1 0-4zm8.4 0h6.4a8 8 0 0 1 0 4H13zM7.4 16H11v3.9A8 8 0 0 1 7.4 16zm5.6 0h3.6A8 8 0 0 1 13 19.9z"/></svg>
        www.brivane.com
      </li>
    </ul>

    <address class="address" style="font-style:normal">P.O. Box 48, Harlow Street,<br>Eastfield, Zip Code -20410</address>
  </section>

  <section class="card card-back" aria-label="Business card back">
    <div class="wordmark"><span class="wordmark-dot"></span>Brivane</div>
  </section>

</main>
</body>
</html>
```